Manufacturer Needs Custom Decorative Basket Ecommerce Site

We work with local artisans in remote villages around the world to create unique and culturally authentic weaved baskets - decorative, storage, laundry, and handbags.

```html
<!DOCTYPE html>
<html lang="en">
<head>
<meta charset="utf-8">
<title>Willow &amp; Reed</title>
<link href="https://fonts.googleapis.com/css2?family=Roboto:wght@400;500;700&display=swap" rel="stylesheet">
<style>
:root{
  --cream:#f5f1ee;
  --brown:#a57a5c;
  --heading:#a67b5b;
  --ink:#1e1e1e;
  --white:#ffffff;
  --yellow:#ecb812;
  --band:#1f1a17;
  --footer:#1c1c1c;
  --line:#e3ddd8;
}
*{box-sizing:border-box;margin:0;padding:0}
html,body{width:1200px;height:3827px;overflow:hidden}
body{position:relative;background:var(--cream);font-family:'Roboto',sans-serif;color:var(--ink)}
.abs{position:absolute}
a{color:inherit;text-decoration:none}

.site-header{left:0;top:0;width:1200px;height:86px;background:var(--white)}
.search{left:110px;top:30px;display:flex;align-items:center;gap:14px;font-size:14px;letter-spacing:1px;font-weight:500}
.brand{left:0;width:1200px;top:26px;text-align:center;font-size:27px;font-weight:500;letter-spacing:1px}
.header-icons{left:975px;top:28px;display:flex;gap:20px}

.hero{left:0;top:86px;width:1200px;height:599px;
  background:radial-gradient(ellipse at 18% 40%,#c0334a 0,#9c3a3a 12%,transparent 28%),
  linear-gradient(100deg,#8a6f5c 0%,#b89a80 35%,#cdb49a 55%,#bfa58b 75%,#9c8672 100%)}
.hero-shade{left:0;top:86px;width:1200px;height:599px;background:rgba(40,25,15,.25)}
.main-nav{left:0;width:1200px;top:134px;display:flex;justify-content:center;gap:28px;color:var(--white);font-size:17px;font-weight:700}
.hero-kicker{left:0;width:1200px;top:308px;text-align:center;color:var(--white);font-size:17px;font-weight:500}
.hero-title{left:0;width:1200px;top:348px;text-align:center;color:var(--white);font-size:60px;font-weight:500;letter-spacing:1px}
.btn{display:flex;align-items:center;justify-content:center;background:var(--brown);color:var(--white);border-radius:28px;font-size:16px;font-weight:500;letter-spacing:.5px}
.hero-btn{left:518px;top:451px;width:164px;height:54px}
.slider-ctrl{left:1124px;top:330px}

.promo{overflow:hidden}
.promo-summer{left:111px;top:781px;width:449px;height:404px;background:linear-gradient(90deg,#ecebea 0%,#e4e2df 55%,#c9a77c 75%,#e2dfdb 100%)}
.promo-sale{left:587px;top:781px;width:499px;height:186px;background:var(--yellow)}
.promo-deals{left:587px;top:998px;width:499px;height:186px;background:linear-gradient(90deg,#a18d7c,#b09c8b 60%,#8fa79e 85%,#a99484)}
.promo-art{position:absolute}
.promo-kicker{font-size:17px;font-weight:500}
.promo-title{font-size:25px;font-weight:500;line-height:30px}
.shop-now{display:flex;align-items:center;gap:14px;font-size:17px;font-weight:700}

.section-title{left:0;width:1200px;text-align:center;color:var(--heading);font-size:38px;font-weight:500}
.card{width:293px;height:316px;background:var(--white);border:1px solid var(--line)}
.card-img{position:absolute;left:0;top:0;width:291px;height:217px}
.card-name{position:absolute;left:0;width:291px;top:243px;text-align:center;font-size:16px}
.card-price{position:absolute;left:0;width:291px;top:272px;text-align:center;font-size:16px}
.card-cart{position:absolute;left:0;width:291px;top:272px;text-align:center;font-size:16px;color:var(--brown);text-decoration:underline}
.view-all{left:518px;width:164px;height:54px}

.band{left:0;top:1936px;width:1200px;height:327px;background:var(--band)}
.band-art{left:683px;top:1936px;width:517px;height:327px;background:radial-gradient(ellipse at 55% 62%,#a3835a 0,#7a5f3e 30%,#3a2d20 58%,transparent 75%)}
.band-title{left:110px;top:1986px;color:var(--white);font-size:33px;font-weight:500;line-height:46px}
.band-sub{left:119px;top:2087px;color:var(--white);font-size:16px}
.band-btn{left:110px;top:2156px;width:163px;height:54px}

.tabs{left:0;width:1200px;top:2441px;display:flex;justify-content:center;gap:46px;font-size:16px}
.tab-active{position:relative}
.tab-active::after{content:"";position:absolute;left:6px;right:6px;bottom:-10px;height:2px;background:var(--brown)}

.site-footer{left:0;top:3435px;width:1200px;height:392px;background:var(--footer);color:var(--white)}
.f-col h4{font-size:16px;font-weight:500;margin-bottom:26px;position:relative}
.f-col h4::after{content:"";position:absolute;left:0;bottom:-14px;width:50px;height:2px;background:var(--brown)}
.f-col li{list-style:none;font-size:16px;line-height:30px}
.contact li{display:flex;gap:12px;align-items:flex-start}
.contact svg{margin-top:8px;flex:none}
.pay{width:42px;height:25px;border-radius:3px}
.f-rule{left:110px;top:3754px;width:980px;height:1px;background:#3d3d3d}
.copyright{left:0;width:1200px;top:3778px;text-align:center;color:var(--white);font-size:16px}
</style>
</head>
<body>

<header class="abs site-header">
  <div class="abs search">
    <svg width="24" height="24" viewBox="0 0 24 24" fill="none" stroke="#333" stroke-width="1.6"><circle cx="10" cy="10" r="7.5"/><line x1="15.5" y1="15.5" x2="22" y2="22"/></svg>
    SEARCH
  </div>
  <div class="abs brand">WILLOW &amp; REED</div>
  <div class="abs header-icons">
    <svg width="24" height="26" viewBox="0 0 24 26" fill="none" stroke="#333" stroke-width="1.5"><path d="M3 8h18l-1.5 16h-15z"/><path d="M8 11V6a4 4 0 0 1 8 0v5"/></svg>
    <svg width="26" height="24" viewBox="0 0 26 24" fill="none" stroke="#333" stroke-width="1.6"><path d="M13 22S2 15 2 8a5.5 5.5 0 0 1 11-1 5.5 5.5 0 0 1 11 1c0 7-11 14-11 14z"/></svg>
    <svg width="24" height="24" viewBox="0 0 24 24" fill="none" stroke="#333" stroke-width="1.5"><circle cx="12" cy="12" r="10.5"/><circle cx="12" cy="9.5" r="3.5"/><path d="M5.5 19.5c1.8-3 4-4 6.5-4s4.7 1 6.5 4"/></svg>
  </div>
</header>

<section class="abs hero" role="img" aria-label="Artisan hands weaving a basket from natural fibres"></section>
<div class="abs hero-shade"></div>
<nav class="abs main-nav"><a>Home</a><a>Category</a><a>Products</a><a>Shop</a><a>Blog</a><a>Contact</a></nav>
<div class="abs hero-kicker">TOP COLLECTIONS</div>
<h1 class="abs hero-title">WILLOW &amp; REED</h1>
<a class="abs btn hero-btn">GET STARTED</a>
<svg class="abs slider-ctrl" width="36" height="104" viewBox="0 0 36 104" fill="none" stroke="#fff" stroke-width="2.2"><polyline points="6,22 18,10 30,22"/><circle cx="18" cy="55" r="2.5" fill="#fff" stroke="none"/><polyline points="6,82 18,94 30,82"/></svg>

<div class="abs promo promo-summer" role="img" aria-label="Woven belly basket with a green plant on a wooden stool against a white brick wall">
  <div class="promo-art" style="left:265px;top:195px;width:140px;height:130px;border-radius:40% 40% 45% 45%;background:#b48d5c"></div>
</div>
<div class="abs" style="left:143px;top:835px">
  <div class="promo-kicker">SUMMER SALE</div>
  <div style="font-size:29px;font-weight:500;line-height:38px;margin-top:12px">NOW SAVE UPTO<br>20%</div>
</div>
<a class="abs shop-now" style="left:143px;top:1122px">SHOP NOW
  <svg width="20" height="10" viewBox="0 0 20 10"><path d="M0 5h16" stroke="#111" stroke-width="2"/><path d="M14 1l5 4-5 4z" fill="#111"/></svg></a>

<div class="abs promo promo-sale" role="img" aria-label="Wicker basket filled with white daisies on a yellow backdrop">
  <div class="promo-art" style="left:310px;top:60px;width:90px;height:100px;border-radius:8px 8px 30px 30px;background:#9b6a3e"></div>
</div>
<div class="abs" style="left:612px;top:801px;color:#fff">
  <div class="promo-kicker">SALE OFF</div>
  <div class="promo-title" style="margin-top:8px">GREAT COLLECTIONS</div>
</div>
<a class="abs shop-now" style="left:612px;top:925px;color:#fff;font-weight:500">SHOP NOW
  <svg width="20" height="10" viewBox="0 0 20 10"><path d="M0 5h16" stroke="#fff" stroke-width="2"/><path d="M14 1l5 4-5 4z" fill="#fff"/></svg></a>

<div class="abs promo promo-deals" role="img" aria-label="Mint green knitted storage basket holding a pink towel"></div>
<div class="abs" style="left:612px;top:1019px;color:#fff">
  <div class="promo-kicker">NEW</div>
  <div class="promo-title" style="margin-top:8px">SHOP TODAY’s DEALS<br>&amp; OFFERS</div>
</div>
<a class="abs shop-now" style="left:612px;top:1144px;color:#fff;font-weight:500">SHOP NOW
  <svg width="20" height="10" viewBox="0 0 20 10"><path d="M0 5h16" stroke="#fff" stroke-width="2"/><path d="M14 1l5 4-5 4z" fill="#fff"/></svg></a>

<h2 class="abs section-title" style="top:1265px">NEW ARRIVALS</h2>

<article class="abs card" style="left:111px;top:1402px">
  <div class="card-img" role="img" aria-label="Orange and yellow striped woven tote basket" style="background:radial-gradient(ellipse at 50% 55%,#e79a28 0,#f0b73a 30%,#fff 55%)"></div>
  <div class="card-name">WILLOW BASKET 01</div><div class="card-price">$49.99</div>
</article>
<article class="abs card" style="left:453px;top:1402px">
  <div class="card-img" role="img" aria-label="Woven seagrass handbag with cut-out handle" style="background:radial-gradient(ellipse at 50% 55%,#a57b57 0,#b99272 30%,#f0f0ef 58%)"></div>
  <div class="card-name">WILLOW BASKET 05</div><div class="card-cart">ADD TO CART</div>
</article>
<article class="abs card" style="left:793px;top:1402px">
  <div class="card-img" role="img" aria-label="Lattice woven wicker basket with handles" style="background:radial-gradient(ellipse at 50% 60%,#d9ac7a 0,#e6c49c 30%,#fff 55%)"></div>
  <div class="card-name">WILLOW BASKET 03</div><div class="card-price">$49.99</div>
</article>

<a class="abs btn view-all" style="top:1786px">VIEW ALL</a>

<section class="abs band"></section>
<div class="abs band-art" role="img" aria-label="Large woven belly basket on a dark background"></div>
<h2 class="abs band-title">YOUR BEST SOURCE OF<br>HANDMADE BASKETS</h2>
<p class="abs band-sub">Products made with love.</p>
<a class="abs btn band-btn">VIEW ALL</a>

<h2 class="abs section-title" style="top:2353px">HANDMADE FOR YOU</h2>
<div class="abs tabs"><span class="tab-active">FEATURED</span><span>TRENDING</span><span>BEST SELLER</span></div>

<article class="abs card" style="left:111px;top:2544px">
  <div class="card-img" role="img" aria-label="Tall lattice wicker basket with looped handles" style="background:radial-gradient(ellipse at 50% 55%,#dcae7c 0,#e9c9a0 28%,#fff 52%)"></div>
  <div class="card-name">WILLOW BASKET 01</div><div class="card-price">$49.99</div>
</article>
<article class="abs card" style="left:453px;top:2544px">
  <div class="card-img" role="img" aria-label="Round shallow wicker bread basket" style="background:radial-gradient(ellipse at 50% 45%,#e5a95e 0,#eec48c 32%,#fff 58%)"></div>
  <div class="card-name">WILLOW BASKET 05</div><div class="card-cart">ADD TO CART</div>
</article>
<article class="abs card" style="left:793px;top:2544px">
  <div class="card-img" role="img" aria-label="Straw tote bag with brown leather handles" style="background:radial-gradient(ellipse at 50% 58%,#b59f7d 0,#cbb99a 30%,#fff 55%)"></div>
  <div class="card-name">WILLOW BASKET 03</div><div class="card-price">$49.99</div>
</article>

<article class="abs card" style="left:111px;top:2908px">
  <div class="card-img" role="img" aria-label="Half-moon rattan bag with round handle" style="background:radial-gradient(ellipse at 50% 52%,#cf9a58 0,#ddb27b 32%,#fff 58%)"></div>
  <div class="card-name">WILLOW BASKET 01</div><div class="card-price">$49.99</div>
</article>
<article class="abs card" style="left:453px;top:2908px">
  <div class="card-img" role="img" aria-label="Wicker picnic basket with tall arched handle" style="background:radial-gradient(ellipse at 50% 60%,#d49b55 0,#e2b77e 30%,#fff 56%)"></div>
  <div class="card-name">WILLOW BASKET 05</div><div class="card-cart">ADD TO CART</div>
</article>
<article class="abs card" style="left:793px;top:2908px">
  <div class="card-img" role="img" aria-label="Pair of square seagrass storage baskets" style="background:radial-gradient(ellipse at 50% 55%,#97794e 0,#b0956c 32%,#f4f3f1 60%)"></div>
  <div class="card-name">WILLOW BASKET 03</div><div class="card-price">$49.99</div>
</article>

<a class="abs btn view-all" style="top:3285px">VIEW ALL</a>

<footer class="abs site-footer"></footer>
<div class="abs f-col" style="left:160px;top:3480px;color:#fff">
  <h4>QUICK LINKS</h4>
  <ul><li>Home</li><li>Category</li><li>Products</li><li>Shop</li><li>Blog</li><li>Contact</li></ul>
</div>
<div class="abs f-col" style="left:340px;top:3480px;color:#fff">
  <h4>EXTRAS</h4>
  <ul><li>Our Brands</li><li>Special Offers</li><li>Gift Vouchers</li><li>Affiliates</li></ul>
</div>
<div class="abs f-col contact" style="left:527px;top:3480px;color:#fff">
  <h4>EXTRAS</h4>
  <ul>
    <li><svg width="14" height="14" viewBox="0 0 14 14" fill="none" stroke="#fff" stroke-width="1.5"><circle cx="7" cy="7" r="6"/><path d="M7 3.5V7h3"/></svg>Monday - Friday: 09:00 - 18:30</li>
    <li><svg width="14" height="16" viewBox="0 0 14 16"><path d="M7 0a5 5 0 0 1 5 5c0 4-5 10-5 10S2 9 2 5a5 5 0 0 1 5-5z" fill="#fff"/><circle cx="7" cy="5" r="2" fill="#1c1c1c"/></svg><span>48 Harbor Lane, Brookfield<br>district</span></li>
    <li><svg width="14" height="14" viewBox="0 0 14 14"><path d="M3 1l2.5 3-1.5 1.5c.8 1.8 2.2 3.2 4 4L9.5 8 13 10.5 11.5 13C6 13 1 8 1 2.5z" fill="#fff"/></svg>+1-555-014-2277</li>
    <li><svg width="16" height="12" viewBox="0 0 16 12" fill="none" stroke="#fff" stroke-width="1.4"><rect x="1" y="1" width="14" height="10"/><path d="M1 1l7 6 7-6"/></svg>hello@willowreed.example</li>
  </ul>
</div>
<div class="abs f-col" style="left:845px;top:3480px;color:#fff">
  <h4>PAYMENT OPTIONS</h4>
</div>
<div class="abs" style="left:842px;top:3548px;display:grid;grid-template-columns:repeat(4,42px);gap:8px 7px">
  <div class="pay" style="background:#2b6cb8"></div><div class="pay" style="background:#3a8fd0"></div><div class="pay" style="background:#2d4aa3"></div><div class="pay" style="background:#e05a2a"></div>
  <div class="pay" style="background:#f2f2f2"></div><div class="pay" style="background:#e8e8e8"></div><div class="pay" style="background:#f2f2f2"></div><div class="pay" style="background:#f4f4f4"></div>
  <div class="pay" style="background:#e6e6e6"></div><div class="pay" style="background:#2a3a6a"></div><div class="pay" style="background:#1f3b8a"></div>
</div>
<div class="abs f-rule"></div>
<div class="abs copyright">2021 Willow &amp; Reed. All Rights Reserved.</div>

</body>
</html>
```